Social Media Graphics - Copperfield Loop

Create 6-7 individual social media graphics (square size) to encourage folks to join our online course, using either of the text below (only one set of text per graphic:

The Lantern Ridge Method
How to Create a 7-Figure Business From Scratch
Sign Up Today!

Or

The Lantern Ridge Method
Fast-track Your Way to a Multi-Million Business!
Sign Up Today!

For the color scheme of the graphics, use 1 or 2 colors in the color palette attached; or use any colors that look nice with their outfits; AVOID using red, white and blue altogether because it will look like an Independence Day (4th of July) graphic and we don’t want that; make sure the graphics appeal to both men and women

Make sure each graphic contains 1 of the 2 pics attached; and make sure one of the graphics is all TEXT only.

Target Market(s)

men and women looking to make more money

Industry/Entity Type

entrepreneurship

Requirements
Must have
• see the text document attached
Nice to have
• We are open to a nice color design; the color palette colors are not required, especially we don't want red, white and blue used together
Should not have
• AVOID using red, white and blue altogether because it will look like an Independence Day (4th of July) graphic and we dont want that

```html
<!DOCTYPE html>
<html lang="en">
<head>
<meta charset="utf-8">
<title>The Lantern Ridge Method – Sign Up</title>
<link rel="stylesheet" href="https://fonts.googleapis.com/css2?family=Montserrat:wght@300;400;700;800&display=swap">
<style>
  :root {
    --paper: #ffffff;
    --royal: #11159c;
    --navy: #020680;
    --navy-deep: #0c1257;
    --stripe: #0a0c92;
    --gold: #fcc200;
    --gold-light: #fbd97a;
    --ink: #050a78;
  }
  * { margin: 0; padding: 0; box-sizing: border-box; }
  html, body { width: 1200px; height: 1200px; overflow: hidden; background: var(--paper); }
  .post {
    position: relative;
    width: 1200px;
    height: 1200px;
    font-family: "Montserrat", sans-serif;
    color: var(--paper);
  }
  .backdrop { position: absolute; inset: 0; }
  .content {
    position: absolute;
    inset: 0;
    text-align: center;
  }
  .title {
    position: absolute;
    top: 262px;
    left: 0;
    right: 0;
    font-weight: 800;
    line-height: 1;
  }
  .title-lead {
    display: block;
    font-size: 80px;
    letter-spacing: -0.5px;
  }
  .title-accent {
    display: block;
    margin-top: 22px;
    font-size: 112px;
    color: var(--gold);
    letter-spacing: -1px;
  }
  .rule {
    position: absolute;
    left: 562px;
    width: 74px;
    height: 5px;
    background: var(--gold);
  }
  .rule-top { top: 528px; }
  .rule-bottom { top: 821px; }
  .tagline {
    position: absolute;
    top: 596px;
    left: 0;
    right: 0;
    font-weight: 400;
    font-size: 42px;
    line-height: 57px;
    letter-spacing: 5px;
  }
  .tagline strong { font-weight: 800; letter-spacing: 3px; }
  .cta {
    position: absolute;
    left: 446px;
    top: 899px;
    width: 307px;
    height: 53px;
    border-radius: 27px;
    background: linear-gradient(180deg, var(--gold-light) 0%, var(--gold) 70%);
    color: var(--ink);
    font-weight: 800;
    font-size: 29px;
    line-height: 53px;
    letter-spacing: -0.5px;
  }
</style>
</head>
<body>
<main class="post">
  <svg class="backdrop" width="1200" height="1200" viewBox="0 0 1200 1200" aria-hidden="true">
    <defs>
      <linearGradient id="band-fill" x1="0" y1="0" x2="1" y2="1">
        <stop offset="0" stop-color="#1a1fa8"/>
        <stop offset="0.45" stop-color="#020680"/>
        <stop offset="0.8" stop-color="#0c1257"/>
        <stop offset="1" stop-color="#0a0d6a"/>
      </linearGradient>
      <linearGradient id="stripe-fill" x1="0" y1="0" x2="1" y2="0">
        <stop offset="0" stop-color="#1a20a8"/>
        <stop offset="0.35" stop-color="#0a0c92"/>
        <stop offset="1" stop-color="#0a0c92"/>
      </linearGradient>
      <clipPath id="band-shape">
        <path d="M517 0 H1200 V923 L754 1200 H0 V331 L475 37 Q500 20 517 0 Z"/>
      </clipPath>
    </defs>
    <rect width="1200" height="1200" fill="var(--paper)"/>
    <g clip-path="url(#band-shape)">
      <rect width="1200" height="1200" fill="url(#band-fill)"/>
      <circle class="orb-top" cx="1010" cy="-20" r="470" fill="#020680" opacity="0.85"/>
      <circle class="orb-left" cx="128" cy="128" r="182" fill="#030885" opacity="0.9"/>
      <circle class="mound-low" cx="160" cy="990" r="330" fill="#060a6c" opacity="0.55"/>
      <path class="sweep-light" d="M437 1200 Q480 1140 557 1087 L1200 718 V1200 Z" fill="url(#stripe-fill)"/>
      <path class="sweep-inner" d="M480 1200 Q510 1170 560 1140 L1200 770 V1200 Z" fill="#080b8e"/>
    </g>
  </svg>

  <section class="content">
    <h1 class="title">
      <span class="title-lead">The Lantern Ridge</span>
      <span class="title-accent">Method</span>
    </h1>
    <div class="rule rule-top"></div>
    <p class="tagline">How to Create a<br><strong>7-Figure</strong> Business<br>From Scratch</p>
    <div class="rule rule-bottom"></div>
    <div class="cta">Sign Up Today!</div>
  </section>
</main>
</body>
</html>
```